Greeting Card Design - Bright Hearts Open Pages

Hi there

Thank you for taking the time to read about this project.

The project is for a range of greeting cards for the gay and lesbian community. The brand is called "Bright Hearts Open Pages".

In this project I require four designs in total (designs for homosexual couples, two for men and two for women). The designs need to reflect the general concept of being in love.

I am looking for variety (fun and funky, as well as modern and classy - please design to your tastes and I will give feedback).

I will work with each designer closely and provide the words for the cards as the designs are developed.

Thank you for considering this project.
Updates

I'm currently having issues with the pixel harbor website and it won't let me upload files to show the logo. I will do so as soon as the website allows me. Thanks

Target Market(s)

Gay and lesbian community.

Industry/Entity Type

Community

Requirements
Must have
• I am looking for variety in the range. I would like designs that are modern and classy range; and also designs that are fun and funky.
Nice to have
• Hand drawings are good for the fun range, so is colour.
The classy range can be symbolic (e.g. holding hands) or black and whites.
Should not have
• Please do not use rainbows or rainbow coloured font.

```html
<!DOCTYPE html>
<html lang="en">
<head>
<meta charset="utf-8">
<title>Bright Hearts Open Pages – Simply Very Much in Love</title>
<link rel="stylesheet" href="https://fonts.googleapis.com/css2?family=Cormorant+Garamond:wght@500&family=Pinyon+Script&display=swap">
<style>
  :root {
    --paper: #f6f9f9;
    --tag-red: #bd0016;
    --couple-blue: #0a37e8;
    --ink-light: #ffffff;
  }
  html, body {
    margin: 0;
    padding: 0;
    overflow: hidden;
    background: var(--paper);
  }
  .card {
    position: relative;
    width: 1200px;
    height: 859px;
    background: var(--paper);
    overflow: hidden;
    font-family: "Cormorant Garamond", Georgia, serif;
  }
  .brand-tag {
    position: absolute;
    left: 200px;
    top: 289px;
    width: 268px;
    height: 268px;
    border-radius: 50%;
    background: var(--tag-red);
  }
  .brand-tag__hole {
    position: absolute;
    top: 10px;
    left: 127px;
    width: 13px;
    height: 13px;
    border-radius: 50%;
    background: var(--paper);
  }
  .brand-tag__name {
    position: absolute;
    left: 78px;
    top: 180px;
    width: 140px;
    margin: 0;
    color: var(--ink-light);
    font-size: 22px;
    font-weight: 500;
    line-height: 1.05;
    text-align: center;
  }
  .couple-area {
    position: absolute;
    left: 600px;
    top: 64px;
    width: 600px;
    height: 795px;
    background: var(--couple-blue);
    border-radius: 220px 220px 0 0;
  }
  .message {
    position: absolute;
    left: 0;
    top: 0;
    width: 1200px;
    height: 859px;
    color: var(--ink-light);
    pointer-events: none;
  }
  .message__rules {
    position: absolute;
    left: 0;
    top: 0;
  }
  .message__simply {
    position: absolute;
    left: 761px;
    top: 459px;
    margin: 0;
    font-size: 50px;
    font-weight: 500;
    line-height: 1;
  }
  .message__phrase {
    position: absolute;
    left: 761px;
    top: 540px;
    margin: 0;
    font-size: 22px;
    font-weight: 500;
    line-height: 1;
  }
  .message__love {
    position: absolute;
    left: 922px;
    top: 501px;
    margin: 0;
    font-family: "Pinyon Script", cursive;
    font-size: 100px;
    font-weight: 400;
    line-height: 1;
  }
</style>
</head>
<body>
  <main class="card">
    <div class="brand-tag">
      <span class="brand-tag__hole"></span>
      <p class="brand-tag__name">Bright Hearts<br>Open Pages</p>
    </div>

    <div class="couple-area" role="img" aria-label="Blue silhouette of a couple embracing, about to kiss"></div>

    <div class="message">
      <svg class="message__rules" width="1200" height="859" viewBox="0 0 1200 859" aria-hidden="true">
        <g stroke="var(--ink-light)" stroke-width="2">
          <line x1="733" y1="514" x2="1082" y2="514"/>
          <line x1="733" y1="583" x2="1082" y2="583"/>
        </g>
      </svg>
      <p class="message__simply">SIMPLY</p>
      <p class="message__phrase">very much in</p>
      <p class="message__love">love</p>
    </div>
  </main>
</body>
</html>
```